Commercial photographer, UAV drone photography & 360 walk-through visuals

I need a business card design that is minimalist but yet pretentiously creative. My target market are architects, designers, advertising agents and marketing managers. It is important to stress that though I am asking for a minimalist design it needs to have creative impact.

Target Market(s)

Architects, interiors designers, web-designers, artists

Contact Information for Business Card

Include my name, mobile [cell] number, email, web page and the company logo. Do not to include a postal address.

Colors

Designer to choose colors to be used in the design.

Requirements
Must have
• The following information is to be included:
• Milo Fenwick
• Photographer
• m: 07812 593174
• e: milo@mfimagery.co.uk
• w: mfimagery.co.uk

```html
<!DOCTYPE html>
<html lang="en">
<head>
<meta charset="utf-8">
<title>MF Imagery – Business Card</title>
<link rel="stylesheet" href="https://fonts.googleapis.com/css2?family=Arimo:wght@400;700&family=Parisienne&display=swap">
<style>
  :root {
    --backdrop: #2a2a2a;
    --card-white: #eeeff2;
    --card-black: #0d0d0e;
    --ink: #111111;
    --ink-soft: #333333;
    --paper-text: #f4f4f4;
  }
  * { margin: 0; padding: 0; box-sizing: border-box; }
  html, body {
    width: 1200px; height: 1200px; overflow: hidden;
    background: var(--backdrop);
  }
  .canvas {
    width: 1200px; height: 1200px;
    display: flex; flex-direction: column;
    align-items: center; justify-content: center; gap: 60px;
  }
  .card {
    position: relative;
    width: 760px; height: 490px;
    overflow: hidden;
    font-family: 'Arimo', Arial, sans-serif;
  }
  /* Front side */
  .card--front {
    background: var(--card-white);
    color: var(--ink);
  }
  .front__name-block {
    position: absolute; top: 62px; left: 0; right: 0;
    text-align: center;
  }
  .front__name {
    display: inline-block;
    font-size: 40px; font-weight: 400;
    letter-spacing: 0.5px;
    padding: 0 6px 3px;
    border-bottom: 1.5px solid var(--ink);
  }
  .front__name strong { font-weight: 700; }
  .front__role {
    font-family: 'Parisienne', cursive;
    font-size: 17px; color: var(--ink-soft);
    margin-top: 2px;
  }
  .front__contact {
    position: absolute; top: 196px; left: 0; right: 0;
    text-align: center;
    font-size: 26px; line-height: 1.15;
  }
  .front__brand {
    position: absolute; top: 282px; left: 0; right: 0;
    display: flex; justify-content: center; align-items: center; gap: 10px;
  }
  .brand-mark {
    width: 14px; height: 14px; background: currentColor;
  }
  .brand-name {
    font-size: 26px; font-weight: 400; letter-spacing: 3px;
    text-transform: uppercase;
  }
  .front__band {
    position: absolute; left: 0; right: 0; top: 345px; height: 42px;
    background: var(--card-black);
    color: var(--paper-text);
    display: flex; align-items: center; justify-content: center;
    font-size: 20px; letter-spacing: 0.5px;
  }
  /* Back side */
  .card--back {
    background: var(--card-black);
    color: var(--paper-text);
    display: flex; align-items: center; justify-content: center;
  }
  .back__brand {
    display: flex; align-items: center; gap: 18px;
    margin-left: 120px;
  }
  .back__brand .brand-mark { width: 26px; height: 26px; }
  .back__brand .brand-name { font-size: 58px; letter-spacing: 6px; }
</style>
</head>
<body>
<main class="canvas">
  <section class="card card--front" aria-label="Business card front">
    <div class="front__name-block">
      <h1 class="front__name"><strong>Milo</strong> Fenwick</h1>
      <p class="front__role">Photographer</p>
    </div>
    <p class="front__contact">07812 593174<br>milo@mfimagery.co.uk</p>
    <div class="front__brand">
      <span class="brand-mark" aria-hidden="true"></span>
      <span class="brand-name">MF Imagery</span>
    </div>
    <div class="front__band">mfimagery.co.uk</div>
  </section>

  <section class="card card--back" aria-label="Business card back">
    <div class="back__brand">
      <span class="brand-mark" aria-hidden="true"></span>
      <span class="brand-name">MF Imagery</span>
    </div>
  </section>
</main>
</body>
</html>
```